bright harbour crest Need a flyer ,ticket and banner design

childrent christmas party 2015
venue : korvane plaza block 5 #04-119
singapore 047215

hi would like to get a design before sunday take note for the banner flyerthe theme will be (blue/gold)for ticket will attach sample here.here 3 sample

```html
<!DOCTYPE html>
<html lang="en">
<head>
<meta charset="utf-8">
<title>Christmas Party Tickets</title>
<link rel="stylesheet" href="https://fonts.googleapis.com/css2?family=Exo+2:ital,wght@1,600&family=Oswald:wght@500;600;700&family=Open+Sans:wght@600;700&family=Raleway:wght@300;500&family=Pinyon+Script&family=Arimo:wght@700&display=swap">
<style>
  :root {
    --bg-top: #262425;
    --bg-bottom: #626262;
    --snow-light: #e4f1f8;
    --snow-mid: #a9cfe2;
    --panel-deep: #0a57a8;
    --panel-light: #3c9ad8;
    --stub-navy: #0e0b5a;
    --stub-sky: #4a9fdc;
    --ink-white: #ffffff;
    --ink-navy: #0e1a4a;
    --ink-dark: #111111;
    --date-grey: #e6e6e6;
  }
  html, body {
    margin: 0;
    padding: 0;
    width: 1200px;
    height: 1200px;
    overflow: hidden;
  }
  body {
    background: linear-gradient(180deg, var(--bg-top) 0%, var(--bg-bottom) 100%);
  }
  .sheet { display: block; width: 1200px; height: 1200px; }
  .sheet-title { font-family: "Exo 2", sans-serif; font-style: italic; font-weight: 600; fill: var(--ink-white); }
  .headline { font-family: "Oswald", sans-serif; font-weight: 600; }
  .gold { fill: url(#gold-foil); }
  .condensed { font-family: "Oswald", sans-serif; font-weight: 500; fill: var(--ink-white); }
  .info { font-family: "Open Sans", sans-serif; font-weight: 700; fill: var(--ink-white); }
  .date-day { font-family: "Open Sans", sans-serif; font-weight: 600; fill: var(--date-grey); }
  .rule { stroke: var(--ink-white); stroke-width: 2; }
  .brand-name { font-family: "Oswald", sans-serif; font-weight: 500; fill: var(--ink-white); }
  .script { font-family: "Pinyon Script", cursive; fill: var(--ink-white); }
  .banner-word { font-family: "Oswald", sans-serif; font-weight: 700; fill: var(--ink-white); }
  .ribbon-text { font-family: "Arimo", sans-serif; font-weight: 700; fill: var(--ink-dark); }
  .admit { font-family: "Raleway", sans-serif; font-weight: 300; fill: var(--ink-navy); }
  .fine { font-family: "Raleway", sans-serif; font-weight: 500; fill: var(--ink-navy); }
  .rule-navy { stroke: var(--ink-navy); stroke-width: 1.5; }
  .perforation { stroke: var(--ink-navy); stroke-width: 2; stroke-dasharray: 6 4; }
</style>
</head>
<body>
<svg class="sheet" viewBox="0 0 1200 1200" xmlns="http://www.w3.org/2000/svg">
  <defs>
    <linearGradient id="gold-foil" x1="0" y1="0" x2="0" y2="1">
      <stop offset="0" stop-color="#f7e39a"/>
      <stop offset="0.5" stop-color="#c8952f"/>
      <stop offset="1" stop-color="#f1cf78"/>
    </linearGradient>
    <linearGradient id="snow-fill" x1="0" y1="0" x2="1" y2="1">
      <stop offset="0" stop-color="var(--snow-light)"/>
      <stop offset="1" stop-color="var(--snow-mid)"/>
    </linearGradient>
    <radialGradient id="panel-fill" cx="0.6" cy="0.45" r="0.7">
      <stop offset="0" stop-color="var(--panel-light)"/>
      <stop offset="1" stop-color="var(--panel-deep)"/>
    </radialGradient>
    <linearGradient id="photo-fill" x1="0" y1="0" x2="1" y2="1">
      <stop offset="0" stop-color="#2f3a22"/>
      <stop offset="0.5" stop-color="#5a4a3a"/>
      <stop offset="1" stop-color="#3c5a30"/>
    </linearGradient>
    <path id="arc-christmas" d="M262,878 Q462,836 664,890"/>
    <path id="arc-ribbon" d="M276,944 Q462,892 650,946"/>
  </defs>

  <text class="sheet-title" x="600" y="106" font-size="74" text-anchor="middle">Tickets</text>

  <!-- Party ticket -->
  <g class="ticket ticket-party">
    <path d="M110,154 H795 L810,168 V572 L795,586 H110 Z" fill="url(#snow-fill)" role="img" aria-label="Snow texture border"/>
    <rect x="150" y="189" width="620" height="362" fill="url(#panel-fill)"/>

    <text class="headline gold" x="182" y="292" font-size="92" textLength="552" lengthAdjust="spacingAndGlyphs">CHRISTMAS PARTY</text>

    <text class="condensed" x="300" y="344" font-size="36" text-anchor="end">1 CHILL</text>
    <text class="condensed" x="300" y="376" font-size="36" text-anchor="end">1 ADULT</text>
    <text class="headline" x="316" y="374" font-size="80" fill="#111" textLength="94" lengthAdjust="spacingAndGlyphs">$22</text>

    <text class="condensed" x="434" y="356" font-size="52" textLength="298" lengthAdjust="spacingAndGlyphs">KORVANE PLAZA</text>

    <line class="rule" x1="436" y1="386" x2="516" y2="386"/>
    <line class="rule" x1="436" y1="440" x2="516" y2="440"/>
    <text class="info" x="436" y="428" font-size="42" textLength="80" lengthAdjust="spacingAndGlyphs">DEC</text>
    <text class="date-day" x="522" y="444" font-size="104" textLength="106" lengthAdjust="spacingAndGlyphs">19</text>
    <line class="rule" x1="636" y1="386" x2="732" y2="386"/>
    <line class="rule" x1="636" y1="440" x2="732" y2="440"/>
    <text class="info" x="636" y="428" font-size="42" textLength="96" lengthAdjust="spacingAndGlyphs">2015</text>

    <text class="info" x="574" y="488" font-size="29" text-anchor="end">BLOCK 5</text>
    <text class="info" x="574" y="518" font-size="29" text-anchor="end">#04-119</text>
    <line class="rule" x1="592" y1="460" x2="592" y2="520"/>
    <text class="info" x="610" y="488" font-size="29">2:00 TO</text>
    <text class="info" x="610" y="518" font-size="29">6:00 PM</text>

    <g class="brand">
      <rect x="283" y="410" width="28" height="28" fill="#e8c35a"/>
      <text class="brand-name" x="297" y="474" font-size="22" text-anchor="middle">BRIGHT HARBOUR</text>
      <text class="brand-name" x="297" y="500" font-size="22" text-anchor="middle">CREST</text>
    </g>

    <path d="M810,168 L824,154 H1088 V588 H824 L810,574 Z" fill="var(--stub-navy)"/>
    <line x1="812" y1="170" x2="812" y2="572" stroke="#8fb6d8" stroke-width="2" stroke-dasharray="6 4"/>

    <text class="headline gold" transform="translate(902,560) rotate(-90)" font-size="62" textLength="376" lengthAdjust="spacingAndGlyphs">CHRISTMAS PARTY</text>
    <g transform="translate(972,520) rotate(-90)">
      <line class="rule" x1="0" y1="-44" x2="0" y2="8" transform="rotate(90)" stroke-opacity="0"/>
      <line class="rule" x1="0" y1="-44" x2="80" y2="-44"/>
      <line class="rule" x1="0" y1="8" x2="80" y2="8"/>
      <text class="info" x="0" y="0" font-size="42" textLength="80" lengthAdjust="spacingAndGlyphs">DEC</text>
      <text class="date-day" x="104" y="16" font-size="104" textLength="92" lengthAdjust="spacingAndGlyphs">19</text>
      <line class="rule" x1="200" y1="-44" x2="296" y2="-44"/>
      <line class="rule" x1="200" y1="8" x2="296" y2="8"/>
      <text class="info" x="200" y="0" font-size="42" textLength="96" lengthAdjust="spacingAndGlyphs">2015</text>
    </g>
    <text class="info" transform="translate(1026,496) rotate(-90)" font-size="30" textLength="248" lengthAdjust="spacingAndGlyphs">BLOCK 5 #04-119</text>
    <text class="info" transform="translate(1060,486) rotate(-90)" font-size="30" textLength="226" lengthAdjust="spacingAndGlyphs">2:00 TO 6:00 PM</text>
  </g>

  <!-- Greeting ticket -->
  <g class="ticket ticket-greeting">
    <path d="M110,638 H795 L810,652 V1058 L795,1072 H110 Z" fill="url(#snow-fill)" role="img" aria-label="Snow texture border"/>
    <rect x="150" y="674" width="620" height="364" fill="url(#photo-fill)" role="img" aria-label="Photo of a child opening a present in front of a lit Christmas tree"/>

    <line class="rule" x1="342" y1="756" x2="362" y2="756"/>
    <text class="script" x="460" y="766" font-size="66" text-anchor="middle">Merry</text>
    <line class="rule" x1="558" y1="756" x2="578" y2="756"/>

    <text class="banner-word" font-size="86"><textPath href="#arc-christmas" textLength="398" lengthAdjust="spacingAndGlyphs">CHRISTMAS</textPath></text>

    <path d="M236,906 Q462,844 688,908 L676,962 Q462,904 248,960 Z" fill="var(--ink-white)"/>
    <text class="ribbon-text" font-size="44"><textPath href="#arc-ribbon" textLength="372" lengthAdjust="spacingAndGlyphs">HAPPY NEW YEAR</textPath></text>

    <path d="M810,652 L824,638 H1088 V1072 H824 L810,1058 Z" fill="var(--stub-sky)"/>
    <line class="perforation" x1="812" y1="654" x2="812" y2="1056"/>

    <text class="headline gold" transform="translate(902,1044) rotate(-90)" font-size="62" textLength="376" lengthAdjust="spacingAndGlyphs">CHRISTMAS PARTY</text>
    <text class="admit" transform="translate(968,1040) rotate(-90)" font-size="54" textLength="360" lengthAdjust="spacing">ADMIT ONE</text>
    <line class="rule-navy" x1="982" y1="682" x2="982" y2="1034"/>
    <text class="fine" transform="translate(1002,1026) rotate(-90)" font-size="14" textLength="330" lengthAdjust="spacing">PRICE $22 · SAT · DEC 19 · 2-6PM</text>
    <line class="rule-navy" x1="1015" y1="682" x2="1015" y2="1034"/>
    <text class="fine" transform="translate(1040,1048) rotate(-90)" font-size="14" textLength="376" lengthAdjust="spacing">RESERVED THE RIGHT OF ADMISSION</text>
  </g>
</svg>
</body>
</html>
```